Need a FLAT UI design for mobile campus Marketplace APP

We need to improve our current UI/UX design for a mobile application called Tradora. It is designed for students to buy and sell their goods, such as books and furnitures, on their own campus to save living expenses. Our initial design does not look very flat and clear enough. We would like to see a flat design improvement for a better purchasing and selling experience using yellow as theme color.

Target Market(s)

college students

Industry/Entity Type

Marketplace

Colors
ffc214
ffcf3e
fee18a
fff3d1

Requirements
Must have
• an improved UI look, flat and simple.
Nice to have
• alternative designs
Should not have
• a new function design for the app on the design

```html
<!DOCTYPE html>
<html lang="en">
<head>
<meta charset="utf-8">
<title>Tradora – Home</title>
<link rel="stylesheet" href="https://fonts.googleapis.com/css2?family=Open+Sans:wght@300;400&display=swap">
<style>
  :root {
    --theme-yellow: #ffc214;
    --screen-dark: #231f20;
    --footer-grey: #e6e7e9;
    --white: #ffffff;
    --ink: #231f20;
    --muted: #c7c8ca;
    --dot-active: #bcbec0;
    --green-light: #8cc63f;  --green-dark: #3ab54a;
    --orange-light: #fbb040; --orange-dark: #f7941d;
    --taupe-light: #998675;  --taupe-dark: #736357;
    --pink-light: #ee2a7b;   --pink-dark: #da1c5c;
    --blue-light: #27aae1;   --blue-dark: #1c75bc;
    --purple-light: #a186be; --purple-dark: #662d91;
  }
  * { box-sizing: border-box; margin: 0; padding: 0; }
  html, body { width: 690px; height: 1200px; overflow: hidden; }
  body {
    font-family: "Open Sans", Arial, sans-serif;
    font-weight: 300;
    background: var(--footer-grey);
    position: relative;
  }
  .app-header {
    position: absolute; left: 0; top: 0;
    width: 690px; height: 132px;
    background: var(--theme-yellow);
  }
  .status-bar {
    position: absolute; right: 14px; top: 6px;
    display: flex; align-items: center; gap: 6px;
    font-weight: 400; font-size: 24px; color: var(--ink);
  }
  .search-field {
    position: absolute; left: 37px; top: 54px;
    width: 617px; height: 63px;
    background: var(--white);
    border-radius: 11px;
    display: flex; align-items: center;
  }
  .search-icon { position: absolute; left: 20px; top: 14px; }
  .search-placeholder {
    position: absolute; left: 87px; top: 8px;
    font-size: 37px; color: var(--muted);
  }
  .search-clear { position: absolute; right: 18px; top: 16px; }
  .home-screen {
    position: absolute; left: 0; top: 132px;
    width: 690px; height: 968px;
    background: var(--screen-dark);
  }
  .brand-banner {
    position: absolute; left: 0; top: 200px; width: 690px;
    text-align: center;
    font-size: 60px; font-weight: 300; color: var(--white);
  }
  .banner-dots {
    position: absolute; left: 0; top: 389px; width: 690px;
    display: flex; justify-content: center; gap: 8px;
  }
  .banner-dot { width: 20px; height: 20px; border-radius: 50%; background: var(--white); }
  .banner-dot.is-active { background: var(--dot-active); }
  .category-grid {
    position: absolute; left: 0; top: 477px; width: 690px;
    list-style: none;
  }
  .category {
    position: absolute; width: 227px; text-align: center;
    font-size: 23px; color: var(--white);
  }
  .category svg { display: block; margin: 0 auto 12px; }
  .category.col-1 { left: 10px; }
  .category.col-2 { left: 238px; }
  .category.col-3 { left: 465px; }
  .category.row-1 { top: 0; }
  .category.row-2 { top: 249px; }
</style>
</head>
<body>
  <header class="app-header">
    <div class="status-bar">
      <svg width="18" height="16" viewBox="0 0 18 16" aria-hidden="true">
        <rect x="0" y="10" width="3" height="6" fill="#231f20"/>
        <rect x="5" y="7" width="3" height="9" fill="#231f20"/>
        <rect x="10" y="4" width="3" height="12" fill="#231f20"/>
        <rect x="15" y="0" width="3" height="16" fill="#231f20"/>
      </svg>
      <span class="status-time">04:23</span>
    </div>
    <div class="search-field">
      <svg class="search-icon" width="36" height="36" viewBox="0 0 36 36" aria-hidden="true">
        <circle cx="14" cy="14" r="10" fill="none" stroke="#c7c8ca" stroke-width="4"/>
        <line x1="21.5" y1="21.5" x2="33" y2="33" stroke="#c7c8ca" stroke-width="6" stroke-linecap="round"/>
      </svg>
      <span class="search-placeholder">Search</span>
      <svg class="search-clear" width="32" height="32" viewBox="0 0 32 32" aria-hidden="true">
        <circle cx="16" cy="16" r="16" fill="#c7c8ca"/>
        <path d="M10 10 L22 22 M22 10 L10 22" stroke="#fff" stroke-width="3.5" stroke-linecap="round"/>
      </svg>
    </div>
  </header>

  <main class="home-screen">
    <h1 class="brand-banner">Tradora Logo</h1>
    <div class="banner-dots">
      <span class="banner-dot is-active"></span>
      <span class="banner-dot"></span>
      <span class="banner-dot"></span>
      <span class="banner-dot"></span>
      <span class="banner-dot"></span>
    </div>

    <ul class="category-grid">
      <li class="category row-1 col-1">
        <svg width="180" height="180" viewBox="0 0 180 180" aria-hidden="true">
          <circle cx="90" cy="90" r="90" fill="var(--green-light)"/>
          <path d="M153.6 26.4 A90 90 0 0 1 26.4 153.6 Z" fill="var(--green-dark)"/>
          <path d="M52 48 L90 40 L128 48 L128 56 L52 56 Z" fill="#fff"/>
          <rect x="50" y="60" width="80" height="5" fill="#fff"/>
          <rect x="58" y="70" width="9" height="34" fill="#fff"/>
          <rect x="74" y="70" width="9" height="34" fill="#fff"/>
          <rect x="90" y="70" width="9" height="34" fill="#fff"/>
          <rect x="106" y="70" width="9" height="34" fill="#fff"/>
          <rect x="50" y="108" width="80" height="5" fill="#fff"/>
          <rect x="44" y="117" width="92" height="6" fill="#fff"/>
        </svg>
        Campus Life
      </li>
      <li class="category row-1 col-2">
        <svg width="180" height="180" viewBox="0 0 180 180" aria-hidden="true">
          <circle cx="90" cy="90" r="90" fill="var(--orange-light)"/>
          <path d="M153.6 26.4 A90 90 0 0 1 26.4 153.6 Z" fill="var(--orange-dark)"/>
          <rect x="48" y="62" width="84" height="52" fill="none" stroke="#fff" stroke-width="3"/>
          <rect x="88" y="114" width="4" height="10" fill="#fff"/>
          <rect x="74" y="124" width="32" height="3" fill="#fff"/>
        </svg>
        Electronics
      </li>
      <li class="category row-1 col-3">
        <svg width="180" height="180" viewBox="0 0 180 180" aria-hidden="true">
          <circle cx="90" cy="90" r="90" fill="var(--taupe-light)"/>
          <path d="M153.6 26.4 A90 90 0 0 1 26.4 153.6 Z" fill="var(--taupe-dark)"/>
          <g fill="#fff">
            <rect x="44" y="60" width="8" height="8"/><rect x="60" y="61" width="76" height="5"/>
            <rect x="44" y="77" width="8" height="8"/><rect x="60" y="78" width="76" height="5"/>
            <rect x="44" y="94" width="8" height="8"/><rect x="60" y="95" width="76" height="5"/>
            <rect x="44" y="111" width="8" height="8"/><rect x="60" y="112" width="76" height="5"/>
            <rect x="44" y="128" width="8" height="8"/><rect x="60" y="129" width="76" height="5"/>
          </g>
        </svg>
        Recent
      </li>
      <li class="category row-2 col-1">
        <svg width="180" height="180" viewBox="0 0 180 180" aria-hidden="true">
          <circle cx="90" cy="90" r="90" fill="var(--pink-light)"/>
          <path d="M153.6 26.4 A90 90 0 0 1 26.4 153.6 Z" fill="var(--pink-dark)"/>
          <path d="M50 56 Q70 50 87 58 L87 124 Q70 116 50 120 Z" fill="#fff"/>
          <path d="M130 56 Q110 50 93 58 L93 124 Q110 116 130 120 Z" fill="#fff"/>
          <path d="M46 62 L46 126 Q70 120 90 128 Q110 120 134 126 L134 62" fill="none" stroke="#fff" stroke-width="3"/>
        </svg>
        Books
      </li>
      <li class="category row-2 col-2">
        <svg width="180" height="180" viewBox="0 0 180 180" aria-hidden="true">
          <circle cx="90" cy="90" r="90" fill="var(--blue-light)"/>
          <path d="M153.6 26.4 A90 90 0 0 1 26.4 153.6 Z" fill="var(--blue-dark)"/>
          <path d="M54 44 L126 44 L126 136 L108 122 L90 136 L90 100 L72 114 L54 100 Z" fill="#fff"/>
          <rect x="54" y="66" width="72" height="4" fill="var(--blue-light)"/>
          <rect x="88" y="44" width="4" height="92" fill="var(--blue-light)"/>
        </svg>
        Tickets
      </li>
      <li class="category row-2 col-3">
        <svg width="180" height="180" viewBox="0 0 180 180" aria-hidden="true">
          <circle cx="90" cy="90" r="90" fill="var(--purple-light)"/>
          <path d="M153.6 26.4 A90 90 0 0 1 26.4 153.6 Z" fill="var(--purple-dark)"/>
          <path d="M86 26 L156 136 L26 136 Z" fill="#fff"/>
          <path d="M86 26 L110 80 L26 136 Z" fill="#414042"/>
          <path d="M110 80 L128 110 L40 130 Z" fill="#414042"/>
        </svg>
        Others
      </li>
    </ul>
  </main>
</body>
</html>
```